Velmora Intergrated Marketing Stationary Design Contest

We require a very professional looking stationary set to include: letterhead, compliments slip and business cards (double sided bus cards).

Files should be supplied on either Illustrator or InDesign.

We are interested in perhaps encorporating a faint watermark with the letter q or the logo, but it isnt a pre-requisite

Target Market(s)

Business owners seeking professional marketing services

Industry/Entity Type

Marketing

Requirements
Must have
• Concurrent theme wiht business cards, letterhead and comp slip. Must be an editable document for future ammendment
Should not have
• No use of times new roman or similar fonts

```html
<!DOCTYPE html>
<html lang="en">
<head>
<meta charset="utf-8">
<title>Velmora Integrated Marketing – Stationery Set</title>
<link href="https://fonts.googleapis.com/css2?family=Arimo:wght@400&family=PT+Sans:wght@400&display=swap" rel="stylesheet">
<style>
  :root {
    --grey: #7a7a82;
    --rust: #8a3224;
    --orange: #d45a32;
    --charcoal: #3b3b3d;
    --ink: #222222;
    --rule: #9a9a9a;
    --frame: #b9b9b9;
    --blush: #f4d7cc;
    --paper: #ffffff;
  }
  * { box-sizing: border-box; margin: 0; padding: 0; }
  html, body { width: 1200px; height: 727px; overflow: hidden; background: var(--paper); }
  body { font-family: "Arimo", Arial, sans-serif; color: var(--ink); }
  .sheet-board {
    position: relative; width: 1200px; height: 727px;
    border: 1px solid #d4d4d4;
  }
  .piece { position: absolute; background: var(--paper); border: 1px solid var(--frame); overflow: hidden; }
  .band { position: absolute; }
  .band--grey { background: var(--grey); }
  .band--rust { background: var(--rust); }
  .band--orange { background: var(--orange); }
  .band--charcoal { background: var(--charcoal); }

  .brand { position: absolute; display: flex; align-items: center; gap: 6px; }
  .brand__dot { width: 34px; height: 34px; border-radius: 50%; background: var(--orange); }
  .brand__name { font-size: 30px; letter-spacing: 2px; color: var(--ink); line-height: 1; }

  .divider { position: absolute; width: 1px; background: var(--rule); }
  .info { position: absolute; font-size: 7px; line-height: 7.6px; color: #333; }

  .legal { position: absolute; display: flex; align-items: center; font-family: "PT Sans", Arial, sans-serif; font-size: 9px; color: var(--ink); white-space: nowrap; }
  .legal span { padding: 0 10px; line-height: 20px; }
  .legal span + span { border-left: 1px solid var(--ink); }
  .legal span:first-child { padding-left: 0; }

  /* letterhead */
  .letterhead { left: 39px; top: 33px; width: 513px; height: 662px; border-color: #555; }
  /* compliments slip */
  .comp-slip { left: 601px; top: 40px; width: 572px; height: 249px; }
  /* business card */
  .card { width: 212px; height: 120px; }
  .card--front { left: 601px; top: 345px; }
  .card--back { left: 601px; top: 507px; }
  .card__name { position: absolute; left: 13px; top: 33px; font-size: 9px; line-height: 11px; }
  .card__address { position: absolute; left: 12px; top: 57px; font-size: 6px; line-height: 7.4px; color: #333; }
  .card__contact { position: absolute; left: 0; right: 0; top: 104px; text-align: center; font-size: 6px; line-height: 8px; color: #333; }
  .card__watermark { position: absolute; left: 125px; top: 22px; width: 76px; height: 76px; border-radius: 50%; background: var(--blush); }
</style>
</head>
<body>
<main class="sheet-board">

  <section class="piece letterhead" aria-label="Letterhead">
    <div class="band band--grey" style="left:0;top:0;width:447px;height:18px"></div>
    <div class="band band--rust" style="left:447px;top:0;width:66px;height:18px"></div>
    <div class="band band--orange" style="left:0;top:18px;width:375px;height:25px"></div>
    <div class="band band--charcoal" style="left:375px;top:18px;width:138px;height:25px"></div>

    <div class="brand" style="left:21px;top:52px"><span class="brand__dot"></span><span class="brand__name">velmora</span></div>
    <div class="divider" style="left:197px;top:43px;height:51px"></div>
    <div class="divider" style="left:375px;top:43px;height:51px"></div>
    <p class="info" style="left:220px;top:55px">Velmora Integrated Marketing<br>Harbour Offices<br>Mill Lane<br>Keldon, North Ridings, KN4 7QT</p>
    <p class="info" style="left:400px;top:57px">www.velmoraim.co.uk<br>enquiries@velmoraim.co.uk<br>Tel 01632 960214<br>Fax 01632 960311</p>

    <div class="legal" style="left:71px;top:634px"><span>Company registration&nbsp;&nbsp;&nbsp;4817305</span><span>Vat No 482 1937 55</span><span>Trading as a division of Brantley Ltd</span></div>
  </section>

  <section class="piece comp-slip" aria-label="Compliments slip">
    <div class="band band--grey" style="left:0;top:0;width:497px;height:21px"></div>
    <div class="band band--rust" style="left:497px;top:0;width:75px;height:21px"></div>
    <div class="band band--orange" style="left:0;top:21px;width:418px;height:29px"></div>
    <div class="band band--charcoal" style="left:418px;top:21px;width:154px;height:29px"></div>

    <div class="brand" style="left:26px;top:60px"><span class="brand__dot"></span><span class="brand__name">velmora</span></div>
    <div class="divider" style="left:201px;top:50px;height:48px"></div>
    <div class="divider" style="left:388px;top:50px;height:48px"></div>
    <p class="info" style="left:239px;top:61px;font-size:6.5px;line-height:7px">Velmora Integrated Marketing<br>Harbour Offices<br>Mill Lane<br>Keldon, North Ridings, KN4 7QT</p>
    <p class="info" style="left:443px;top:63px;font-size:6.5px;line-height:7px">www.velmoraim.co.uk<br>enquiries@velmoraim.co.uk<br>Tel 01632 960214<br>Fax 01632 960311</p>

    <div class="legal" style="left:100px;top:220px"><span>Company registration&nbsp;&nbsp;&nbsp;4817305</span><span>Vat No 482 1937 55</span><span>Trading as a division of Brantley Ltd</span></div>
  </section>

  <section class="piece card card--front" aria-label="Business card front">
    <div class="band band--grey" style="left:0;top:0;width:184px;height:7px"></div>
    <div class="band band--rust" style="left:184px;top:0;width:28px;height:7px"></div>
    <div class="band band--orange" style="left:0;top:7px;width:155px;height:12px"></div>
    <div class="band band--charcoal" style="left:155px;top:7px;width:57px;height:12px"></div>
    <div class="card__watermark"></div>
    <p class="card__name">Owen Hartley<br>General Manager</p>
    <p class="card__address">Velmora Integrated Marketing<br>Harbour Offices, Mill Lane<br>Keldon, North Ridings, KN4 7QT</p>
    <p class="card__contact" style="top:102px">www.velmoraim.co.uk owen@velmoraim.co.uk<br>Tel 01632 960214 Fax 01632 960311</p>
  </section>

  <section class="piece card card--back" aria-label="Business card back">
    <div class="brand" style="left:31px;top:42px"><span class="brand__dot" style="width:38px;height:38px"></span><span class="brand__name" style="font-size:31px">velmora</span></div>
  </section>

</main>
</body>
</html>
```